Design an Drama Show poster/ Flyer Advertisement

Need 2 poster & 2x sided flyers design to promote ticket sales of comedy -family drama show.

I have attached 2 word document to guide you in the poster designs
first main promotion design
second dinner and show design

both these design will then be used on both side of a flyer as well with maybe some more info added to dinner & show side.

stick close to the caravan design and you can't go wrong.
attached is also all logo and images that may help.

```html
<!DOCTYPE html>
<html lang="en">
<head>
<meta charset="utf-8">
<title>The Dinner Show – Flyer</title>
<link rel="stylesheet" href="https://fonts.googleapis.com/css2?family=Rye&family=Signika:wght@600&family=Montserrat:wght@400;700&display=swap">
<style>
  :root {
    --page: #d9dadc;
    --ink: #0d0b0c;
    --crimson: #c3174a;
    --crimson-deep: #5a0a1f;
    --price: #ea2a60;
    --white: #ffffff;
    --grey-text: #c9c9c9;
  }
  * { box-sizing: border-box; margin: 0; padding: 0; }
  html, body {
    width: 1200px; height: 1200px; overflow: hidden;
    background: var(--page);
  }
  .flyer {
    position: absolute; left: 210px; top: 50px;
    width: 780px; height: 1100px;
    background: var(--ink);
    overflow: hidden;
  }
  .brand-bar {
    position: absolute; top: 0; height: 108px;
    background: var(--crimson);
    display: flex; align-items: center; justify-content: center; gap: 12px;
    font-family: "Montserrat", sans-serif; font-weight: 700;
    color: var(--ink); font-size: 26px; letter-spacing: 0.5px;
  }
  .brand-bar--company { left: 52px; width: 304px; }
  .brand-bar--package { left: 423px; width: 306px; }
  .brand-dot { width: 30px; height: 30px; border-radius: 50%; background: var(--ink); }

  .hero {
    position: absolute; top: 108px; left: 0; width: 780px; height: 523px;
    background:
      radial-gradient(ellipse 170px 200px at 40px 150px, rgba(255,255,255,0.55), transparent 70%),
      radial-gradient(ellipse 170px 200px at 740px 150px, rgba(255,255,255,0.55), transparent 70%),
      linear-gradient(180deg, #3b3b3b 0%, #6c6c6c 55%, #2a2a2a 100%);
  }
  .hero-band {
    position: absolute; top: 108px; left: 210px; width: 360px; height: 523px;
    background: linear-gradient(180deg, var(--crimson-deep) 0%, #9c1238 45%, var(--crimson) 100%);
    opacity: 0.93;
  }
  .show-title {
    position: absolute; top: 225px; left: 210px; width: 360px;
    text-align: center; font-family: "Rye", serif; color: var(--white);
    line-height: 1.08;
  }
  .show-title .line-small { display: block; font-size: 56px; }
  .show-title .line-large { display: block; font-size: 66px; }
  .title-dots { position: absolute; left: 0; top: 0; }

  .package {
    position: absolute; left: 0; width: 780px;
  }
  .package-badge {
    position: absolute; left: 0; top: 0; width: 121px; height: 72px;
    background: var(--crimson);
    display: flex; align-items: center; justify-content: center;
    font-family: "Montserrat", sans-serif; font-weight: 700;
    font-size: 14px; color: var(--white); text-align: center; line-height: 1.2;
  }
  .package-list {
    position: absolute; left: 145px; top: 10px; list-style: none;
    font-family: "Signika", sans-serif; font-weight: 600;
    font-size: 15px; color: var(--white); line-height: 30px;
  }
  .package-list .price { color: var(--price); }
  .package--one { top: 670px; }
  .package--two { top: 766px; }
  .package--three { top: 861px; }

  .venue-badge {
    position: absolute; left: 356px; top: 964px; width: 64px; height: 64px;
    border-radius: 50%; background: var(--crimson);
    display: flex; align-items: center; justify-content: center;
    font-family: "Montserrat", sans-serif; font-size: 15px; color: var(--white);
  }
  .venue-address {
    position: absolute; left: 0; top: 1040px; width: 780px;
    text-align: center; font-family: "Montserrat", sans-serif;
    font-size: 14px; color: var(--grey-text); line-height: 28px;
    font-style: normal;
  }
</style>
</head>
<body>
  <main class="flyer">
    <div class="brand-bar brand-bar--company"><span class="brand-dot"></span>Harbour Lane Players</div>
    <div class="brand-bar brand-bar--package">Supper &amp; Stage</div>

    <div class="hero" role="img" aria-label="Stage spotlights shining over a dinner table set with glasses and wine bottles"></div>
    <div class="hero-band"></div>
    <svg class="title-dots" width="780" height="640" aria-hidden="true">
      <circle cx="250" cy="300" r="13" fill="var(--crimson)"/>
      <circle cx="469" cy="221" r="11" fill="var(--crimson)"/>
      <circle cx="501" cy="210" r="7" fill="var(--crimson)"/>
    </svg>
    <h1 class="show-title">
      <span class="line-small">THE</span>
      <span class="line-large">DINNER</span>
      <span class="line-large">SHOW</span>
    </h1>

    <section class="package package--one">
      <div class="package-badge">The Copper Wren</div>
      <ul class="package-list">
        <li>·1x Show ticket &amp; delicious two-course pre-show meal. <span class="price">from £22 (BYOB option)</span></li>
        <li>·1x Show ticket &amp; delicious three-course pre-show meal. <span class="price">from £25 (BYOB option)</span></li>
      </ul>
    </section>
    <section class="package package--two">
      <div class="package-badge">Olive &amp; Vine</div>
      <ul class="package-list">
        <li>·1x Show ticket &amp; delicious two-course pre-show meal. <span class="price">from £24</span></li>
        <li>·1x Show ticket &amp; delicious three-course pre-show meal. <span class="price">from £27</span></li>
      </ul>
    </section>
    <section class="package package--three">
      <div class="package-badge">Polly Mae's</div>
      <ul class="package-list">
        <li>·1x Show ticket &amp; delicious two-course pre-show meal. <span class="price">from £20</span></li>
        <li>·1x Show ticket &amp; delicious three-course pre-show meal. <span class="price">from £22</span></li>
      </ul>
    </section>

    <div class="venue-badge">Venue:</div>
    <address class="venue-address">
      Elmfield Parish Church Hall,<br>
      22-26 Market Street, Elmfield BT00 1AB
    </address>
  </main>
</body>
</html>
```